Looking to design a new sign for our church.

Looking for a new sign
4 x 8 feet dimension
We are renaming the church "Medlow Ridge Community Church"
looking for legible graphics
Would like some type of backdrop being a family tree (oak) / open to other ideas as you are led
I have included a pic of the old sign for your review
would like to incorporate our ministry logo on the lower right hand corner of the sign / see file attached

```html
<!DOCTYPE html>
<html lang="en">
<head>
<meta charset="utf-8">
<title>Medlow Ridge Community Church – Sign</title>
<link rel="stylesheet" href="https://fonts.googleapis.com/css2?family=Cinzel:wght@700&family=Arimo:wght@400&display=swap">
<style>
  :root {
    --church-blue: #1d4a87;
    --ink: #1e1e1e;
    --paper: #ffffff;
  }
  * { margin: 0; padding: 0; box-sizing: border-box; }
  html, body {
    width: 1200px;
    height: 998px;
    overflow: hidden;
    background: var(--paper);
  }
  .canvas {
    position: relative;
    width: 1200px;
    height: 998px;
  }
  .sign {
    position: absolute;
    left: 181px;
    top: 286px;
    width: 829px;
    height: 419px;
    border: 8px solid var(--church-blue);
    background: var(--paper);
  }
  .church-name {
    position: absolute;
    left: 0;
    right: 0;
    top: 112px;
    text-align: center;
    font-family: "Cinzel", serif;
    font-weight: 700;
    color: var(--church-blue);
    line-height: 1;
  }
  .church-name__main {
    display: block;
    font-size: 52px;
    letter-spacing: 6px;
  }
  .church-name__sub {
    display: block;
    margin-top: 22px;
    font-size: 34px;
    letter-spacing: 7px;
  }
  .schedule {
    position: absolute;
    left: 59px;
    top: 280px;
    list-style: none;
    font-family: "Arimo", sans-serif;
    font-size: 22px;
    line-height: 32.5px;
    color: var(--ink);
  }
  .ministry-mark {
    position: absolute;
    right: 48px;
    bottom: 34px;
    display: flex;
    flex-direction: column;
    align-items: center;
    gap: 8px;
    width: 120px;
  }
  .ministry-mark__dot {
    width: 44px;
    height: 44px;
    border-radius: 50%;
    background: var(--ink);
  }
  .ministry-mark__name {
    font-family: "Arimo", sans-serif;
    font-size: 13px;
    color: var(--ink);
    text-align: center;
    line-height: 1.2;
  }
</style>
</head>
<body>
  <main class="canvas">
    <section class="sign">
      <h1 class="church-name">
        <span class="church-name__main">Medlow Ridge</span>
        <span class="church-name__sub">Community Church</span>
      </h1>
      <ul class="schedule">
        <li>10:30am Worship Service</li>
        <li>9:30am Sunday School</li>
        <li>6:00pm Wednesday Service</li>
      </ul>
      <div class="ministry-mark">
        <span class="ministry-mark__dot"></span>
        <span class="ministry-mark__name">Crestline Fellowship</span>
      </div>
    </section>
  </main>
</body>
</html>
```